The most amazing design opportunity you will ever get - Plus we may even through in some shares!

We need a new look and feel for our website, something that will knock the socks off our competitors. Something fresh, functional, dynamic and awesome.

Take a look at the attached brief and see if this is something you can get you head around to come up with something just amazing.

Reason: need more designs

A key to your success is to base your design on the Visual Language (colours Black with Orange on white background, integration of cogs, font, style) and remember that our target audience is BUSINESS and the key thing that we are about is INSIGHTS, so if you can include some subtle design that requires insight to use - Perfect!

```html
<!DOCTYPE html>
<html lang="en">
<head>
<meta charset="utf-8">
<title>Northgate Insights</title>
<link href="https://fonts.googleapis.com/css2?family=Open+Sans:ital,wght@0,400;0,600;0,700;1,400&display=swap" rel="stylesheet">
<style>
:root{
  --orange:#f28a30;
  --orange-dark:#e07a20;
  --black:#111;
  --ink:#333;
  --grey:#a9a9a9;
  --tab-bg:#f4f4f4;
  --line:#ccc;
  --white:#fff;
}
*{box-sizing:border-box;margin:0;padding:0}
html,body{width:1007px;height:1200px;overflow:hidden;background:var(--white);font-family:"Open Sans",sans-serif;color:var(--ink)}
.canvas{position:relative;width:1007px;height:1200px}
.abs{position:absolute}
.audience-tabs{left:112px;top:0;width:796px;height:35px;display:flex;background:var(--tab-bg)}
.audience-tabs div{flex:1;display:flex;align-items:center;justify-content:center;gap:5px;color:var(--orange);font-size:12px;border-right:1px solid #ddd}
.audience-tabs div:first-child{background:var(--white);border-right:1px solid var(--orange)}
.stats{left:112px;top:35px;width:796px;height:40px;background:var(--grey);display:flex}
.stats div{flex:1;text-align:center;color:#fff;font-size:9px;line-height:13px;padding-top:8px;border-right:1px solid #bbb}
.stats i{display:block}
.brand{left:112px;top:101px;display:flex;align-items:center;gap:10px}
.brand-mark{width:30px;height:30px;border-radius:50%;background:var(--orange)}
.brand-name{font-size:22px;font-weight:700;color:var(--black);line-height:1}
.notice{left:394px;top:92px;width:514px;height:64px;border:1px solid #ddd;border-radius:5px;overflow:hidden}
.notice h3{background:#b5b5b5;color:#fff;font-weight:400;font-size:12px;height:23px;line-height:23px;padding-left:16px;position:relative}
.notice h3 span{position:absolute;right:10px;top:6px;width:10px;height:10px;border:1px solid #fff;font-size:8px;line-height:8px;text-align:center}
.notice p{font-size:9px;line-height:17px;padding:3px 16px;color:var(--ink)}
.notice p b{float:right;font-weight:400}
.main-nav{left:112px;top:173px;width:796px;height:36px;background:var(--black);display:flex}
.main-nav a{color:#fff;text-decoration:none;font-size:12.5px;display:flex;align-items:center;justify-content:center;border-right:1px solid #333;position:relative}
.main-nav a.active{background:var(--orange)}
.main-nav a.active:after{content:"";position:absolute;bottom:-8px;left:50%;margin-left:-7px;border:7px solid transparent;border-bottom:0;border-top:8px solid var(--orange)}
.section-title{color:var(--orange);font-weight:400;font-size:21px}
.intro{left:129px;top:278px;width:762px;font-size:9px;line-height:17px;color:#555}
.banner{left:121px;top:408px;width:778px;height:260px;border:1px solid var(--line);padding:50px 3px 3px}
.banner .art{width:100%;height:100%;background:linear-gradient(90deg,#4b4fb0,#2a9fe0 20%,#d8232a 50%,#f4b400 70%,#1a9e5b 88%,#26b4c9)}
.pager{right:10px;bottom:10px;display:flex;gap:2px;align-items:center}
.pager span{width:19px;height:18px;background:#333;color:#fff;font-size:11px;text-align:center;line-height:18px}
.pager em{font-style:normal;font-size:11px;padding:0 4px;color:#333}
.profile-card{left:153px;top:228px;width:714px;height:311px;background:rgba(255,255,255,.93);box-shadow:0 0 4px rgba(0,0,0,.25)}
.profile-card header{background:var(--orange);color:#fff;font-size:11px;height:39px;line-height:39px;padding-left:26px}
.avatar{left:24px;top:61px;width:113px;height:120px;background:linear-gradient(#8aa76a,#c99a80)}
.who{left:160px;top:59px}
.who h4{font-weight:400;font-size:12.5px;color:var(--black)}
.who small{font-style:italic;font-size:9px;color:#555;display:block;margin-top:2px}
.stars{margin-top:9px;display:flex;gap:1px}
.tag{display:inline-block;background:var(--orange);color:#fff;font-size:9px;padding:4px 9px;margin-top:6px;border:1px solid var(--orange-dark)}
.tabs{left:26px;top:223px;display:flex;gap:0;font-size:10.5px;color:#555}
.tabs span{margin-right:40px}
.subtabs{left:26px;top:270px;font-size:9.5px;color:#777}
.subtabs span{margin-right:50px}
.on{color:var(--orange)}
.card{top:746px;width:374px;height:260px;border:1px solid var(--line)}
.card .pic{height:130px}
.card h5{color:var(--orange);font-weight:400;font-size:12px;margin:10px 0 0 36px}
.card ul{list-style:none;position:absolute;top:164px;font-size:9.5px;line-height:17px}
.card li{padding-left:13px;position:relative}
.card li:before{content:"";position:absolute;left:0;top:5px;width:5px;height:5px;border:1.5px solid var(--black);border-radius:50%}
.footer-links{left:121px;top:1044px;font-size:9.5px;display:flex;gap:37px}
.social{left:121px;top:1092px;display:flex;gap:5px}
.social span{width:28px;height:28px;border-radius:50%}
.copy{left:121px;top:1150px;font-size:9px;line-height:17px}
.video{left:660px;top:1046px;width:239px;height:135px;background:linear-gradient(135deg,#e23,#fc0 30%,#3ad 60%,#222)}
.video .halo{position:absolute;left:66px;top:12px;width:108px;height:108px;border-radius:50%;background:rgba(255,255,255,.85)}
.video .play{position:absolute;left:100px;top:46px;width:40px;height:30px;border-radius:8px;background:#333}
.video .play:after{content:"";position:absolute;left:16px;top:8px;border-left:11px solid #fff;border-top:7px solid transparent;border-bottom:7px solid transparent}
.video p{position:absolute;bottom:6px;width:100%;text-align:center;color:#fff;font-size:11px}
</style>
</head>
<body>
<div class="canvas">
  <nav class="abs audience-tabs">
    <div>Everyone <svg width="36" height="12"><g fill="#f28a30"><circle cx="4" cy="2" r="2"/><rect x="2" y="4" width="4" height="8"/><circle cx="13" cy="2" r="2" fill="#3ad"/><rect x="11" y="4" width="4" height="8" fill="#3ad"/><circle cx="22" cy="2" r="2" fill="#d33"/><rect x="20" y="4" width="4" height="8" fill="#d33"/><circle cx="31" cy="2" r="2" fill="#5b5"/><rect x="29" y="4" width="4" height="8" fill="#5b5"/></g></svg></div>
    <div>Just Me <svg width="8" height="12"><circle cx="4" cy="2" r="2" fill="#e64"/><rect x="2" y="4" width="4" height="8" fill="#e64"/></svg></div>
    <div>My Friends <svg width="16" height="12"><g fill="#e64"><circle cx="4" cy="2" r="2"/><rect x="2" y="4" width="4" height="8"/><circle cx="12" cy="2" r="2" fill="#f28a30"/><rect x="10" y="4" width="4" height="8" fill="#f28a30"/></g></svg></div>
    <div>My team <svg width="34" height="12"><g><circle cx="4" cy="2" r="2" fill="#e64"/><rect x="2" y="4" width="4" height="8" fill="#e64"/><circle cx="13" cy="2" r="2" fill="#f28a30"/><rect x="11" y="4" width="4" height="8" fill="#f28a30"/><circle cx="22" cy="2" r="2" fill="#5b5"/><rect x="20" y="4" width="4" height="8" fill="#5b5"/><circle cx="31" cy="2" r="2" fill="#3ad"/><rect x="29" y="4" width="4" height="8" fill="#3ad"/></g></svg></div>
  </nav>
  <div class="abs stats">
    <div><i>13,458</i>iMembers</div><div><i>1,700,250</i>iPoints</div><div><i>800,1254</i>iAttributes</div><div><i>600,100</i>iActivity</div><div><i>300, 150</i>iNetworking</div><div><i>i$900,125</i>iDollars</div><div><i>900,000</i>iShares</div>
  </div>

  <div class="abs brand"><span class="brand-mark"></span><span class="brand-name">Northgate Insights</span></div>

  <aside class="abs notice">
    <h3>Noticeborad<span>x</span></h3>
    <p>Lorem ipsum dolor sit amet, consectetur adipisicing elit, sed do eiusmod tempor incididunt ut labore et dolore magna aliqua. Ut enim ad minim veniam... <b>more</b></p>
  </aside>

  <nav class="abs main-nav">
    <a style="width:133px">Insights</a><a class="active" style="width:128px">Profile</a><a style="width:136px">Partner1</a><a style="width:141px">Partner2</a><a style="width:136px">Partner3</a><a style="width:122px;border:0">Home</a>
  </nav>

  <h2 class="abs section-title" style="left:129px;top:234px">Why Insight</h2>
  <p class="abs intro">We are able to help businesses grow and learn collectively, with peers or the help of a specialist. A single portal where you can access solutions and insights across fields. Share your experiences with others, earn points for participation and get recognised as a trusted advisor in the global community, from Starter level through to a Top Guide.</p>
  <h2 class="abs section-title" style="left:129px;top:364px">21 Business Topics</h2>

  <section class="abs banner">
    <div class="art" role="img" aria-label="Colourful interlocking cogs in blue, red, yellow and green"></div>
    <div class="abs pager"><span>1</span><span>2</span><span>3</span><em>......</em><span>20</span><span>21</span><span>22</span><span>&lt;</span><span>&gt;</span></div>
  </section>

  <section class="abs profile-card">
    <header>MAREK DALLOWAY</header>
    <div class="abs avatar" role="img" aria-label="Member profile photo"></div>
    <div class="abs who">
      <h4>@ ADMIN</h4>
      <small>Active 4 Minutes Ago</small>
      <div class="stars"><svg width="64" height="12" viewBox="0 0 64 12"><g stroke="#d9a400" stroke-width=".8"><path id="st" d="M6 .5l1.6 3.6 3.9.4-3 2.6.9 3.8L6 8.9 2.6 10.9l.9-3.8-3-2.6 3.9-.4z" fill="#f6c200"/><use href="#st" x="13"/><use href="#st" x="26"/><use href="#st" x="39" fill="none"/><use href="#st" x="52" fill="none"/></g></svg></div>
      <span class="tag">15005</span><br>
      <span class="tag">Rank - SPECIALIST</span>
    </div>
    <div class="abs tabs"><span>Activity</span><span class="on">Profile</span><span>Notifications(0)</span><span>Friends(45)</span><span>Messages(6)</span><span>groups(2)</span><span>Points(35)</span><span style="margin:0">Settings</span></div>
    <div class="abs subtabs"><span class="on">View</span><span>Edit</span><span>Change Avatar</span></div>
  </section>

  <h2 class="abs section-title" style="left:128px;top:704px">Northgate Insights</h2>

  <article class="abs card" style="left:121px">
    <div class="pic" role="img" aria-label="Silhouettes of celebrating graduates on pink, blue, green and orange stripes" style="background:linear-gradient(90deg,#f3a 0 25%,#2bd 25% 50%,#6d2 50% 75%,#f80 75%)"></div>
    <h5>Target Audience</h5>
    <ul style="left:36px"><li>Graduates</li><li>Solution Providers,</li><li>Job seekers</li><li>Managers</li><li>Executives</li></ul>
    <ul style="left:207px"><li>MBAs</li><li>Authors of business books</li><li>Entrepreneurs</li><li>Specialists</li><li>Employees</li></ul>
  </article>
  <article class="abs card" style="left:525px">
    <div class="pic" role="img" aria-label="Business people walking through a bright glass lobby" style="background:linear-gradient(#2c4a86,#7fa6d8 60%,#1c2c50)"></div>
    <h5>Affiliate Partners</h5>
    <ul style="left:36px"><li>Grad Schools</li><li>University Faculty</li><li>JCompanies</li></ul>
    <ul style="left:207px"><li>Universities</li><li>AJob Portals</li><li>Recruiters</li></ul>
  </article>

  <footer>
    <div class="abs footer-links"><span>Getting Started</span><span>Tutorials</span><span>Insight Points</span><span>Index</span><span>Upcoming Topics</span><span>About us</span></div>
    <div class="abs social"><span style="background:#b22a8c"></span><span style="background:#1a9e3b"></span><span style="background:#7ab8ec"></span><span style="background:#f6d000"></span><span style="background:#f28a30"></span></div>
    <p class="abs copy">Northgate Insights © 2014.<br>All Rights Reserved.</p>
    <div class="abs video" role="img" aria-label="Video thumbnail with colourful arrow pattern">
      <div class="halo"></div><div class="play"></div><p>Our Video</p>
    </div>
  </footer>
</div>
</body>
</html>
```